Überarbeitung/Optimierung eines edlen Layouts für eine Booklet-Seite
Zielgruppe
Diese Booklet-Seite (Vorder- und Rückseite) soll dem Leser übersichtliche Informationen über den Velmer Münster bieten.
Aufgabenstellung
Das bisherige Design (siehe Dateien) gefällt uns schon sehr. Trotzdem fragen wir uns, ob man es noch etwas professioneller gestalten kann? Insbesondere die Überschrift und die Zitate machen uns Sorgen.
Das grundlegende, schlichte Design soll beibehalten werden (weißer Hintergrund, Font 'Open Sans', keine/kaum Design-Elemente bis auf das Logo).
Die Seiten (21x21cm) wurden im Affinity Designer erstellt und sollen für verschiedene Themen (also nicht nur Velmer Münster) das grundlegende Layout vorgeben.

```html
<!DOCTYPE html>
<html lang="de">
<head>
<meta charset="utf-8">
<title>Velmer Münster – Booklet-Seite</title>
<link href="https://fonts.googleapis.com/css2?family=Open+Sans:wght@300;400;600;700&display=swap" rel="stylesheet">
<style>
  :root {
    --stage: #1c1c1c;
    --paper: #ffffff;
    --ink: #4a4a4a;
    --ink-strong: #3a3a3a;
    --rule: #c4c4c4;
    --stone-light: #d8d0bd;
    --stone-mid: #b4aa95;
    --stone-dark: #5f5c55;
    --photo-warm: #a8744a;
    --photo-deep: #4e3220;
    --photo-light: #f2e6d6;
    --drawing-light: #efefef;
    --drawing-mid: #bdbdbd;
  }
  * { box-sizing: border-box; margin: 0; padding: 0; }
  html, body { width: 1200px; height: 2400px; overflow: hidden; }
  body {
    background: var(--stage);
    font-family: "Open Sans", Arial, sans-serif;
    color: var(--ink);
    position: relative;
  }
  .page {
    position: absolute;
    left: 100px;
    width: 1000px;
    height: 1015px;
    background: var(--paper);
    overflow: hidden;
  }
  .page--front { top: 120px; }
  .page--back { top: 1265px; }

  .brand {
    position: absolute;
    width: 140px;
    text-align: right;
    font-weight: 600;
    font-size: 16px;
    line-height: 20px;
    color: var(--ink-strong);
  }

  .title {
    position: absolute; left: 51px; top: 96px;
    font-size: 24px; font-weight: 600; color: var(--ink-strong);
    text-transform: uppercase; letter-spacing: 0.2px;
  }
  .subtitle {
    position: absolute; left: 51px; top: 136px;
    font-size: 14px; font-weight: 700; color: var(--ink-strong);
  }
  .body-text {
    position: absolute;
    font-size: 16px; line-height: 23.6px; font-weight: 300;
    text-align: justify; hyphens: auto;
  }
  .body-text--regular { font-weight: 400; }
  .section-heading {
    position: absolute; font-size: 22px; font-weight: 600;
    color: var(--ink-strong); text-transform: uppercase;
  }
  .quote {
    position: absolute; left: 0;
    border: 1px solid var(--rule); border-left: none;
    display: flex; flex-direction: column; justify-content: center; align-items: center;
    text-align: center;
  }
  .quote__text { font-size: 20px; font-weight: 300; line-height: 25px; color: var(--ink-strong); }
  .quote__source { margin-top: 10px; font-size: 14px; font-weight: 700; color: var(--ink-strong); }

  .visual { position: absolute; }
  .visual--stone {
    background: linear-gradient(180deg, var(--stone-light) 0%, var(--stone-mid) 50%, var(--stone-dark) 58%, #4b4943 100%);
    border-radius: 18px 30px 8px 6px;
  }
  .visual--photo {
    background: linear-gradient(160deg, var(--photo-deep) 0%, var(--photo-warm) 45%, var(--photo-light) 75%, #c99a6c 100%);
  }
  .visual--drawing {
    background: linear-gradient(180deg, var(--drawing-light) 0%, var(--drawing-mid) 60%, var(--drawing-light) 100%);
  }
</style>
</head>
<body>

<section class="page page--front">
  <div class="brand" style="left:812px; top:62px;">Marbeck Edition</div>

  <h1 class="title">Velmer Münster, Stück aus dem Fundament des Südturms</h1>
  <p class="subtitle">Die gewaltigen gotischen Fundamente stammen aus dem 14. Jahrhundert.</p>

  <p class="body-text" style="left:51px; top:228px; width:606px;">Die „Hohe Domkirche Sankt Albanus“ ist weltweit eine der größten Kathedralen und wurde vom Welterbe-Rat zum Weltkulturerbe erklärt. Der monumentale Bau war durch die beiden Türme mit 157 Metern das höchste Bauwerk seiner Zeit und ist heute die meistbesuchte Sehenswürdigkeit Deutschlands. Der Kronenschrein hinter dem Hochaltar ist der größte Reliquienschrein in Europa.</p>

  <div class="quote" style="top:420px; width:657px; height:150px;">
    <p class="quote__text">„Hier, wo der Grundstein liegt, dort mit jenen Türmen<br>zugleich, sollen sich die schönsten Tore der Welt erheben.“</p>
    <p class="quote__source">Friedrich Anselm II, Preußischer König, beim Dombaufest 1842</p>
  </div>

  <div class="visual visual--stone" role="img" aria-label="Freigestelltes Bruchstück aus dem Fundament des Südturms" style="left:717px; top:300px; width:236px; height:339px;"></div>

  <div class="visual visual--photo" role="img" aria-label="Fassade des Velmer Münsters im Gegenlicht, von unten fotografiert" style="left:0; top:665px; width:337px; height:350px;"></div>

  <h2 class="section-heading" style="left:405px; top:714px;">Grundsteinlegung 1248</h2>
  <p class="body-text body-text--regular" style="left:405px; top:760px; width:543px;">Nach der ersten Grundsteinlegung 1248 dauerte es über 600 Jahre bis zur Fertigstellung dieses gotischen Meisterwerks im Jahr 1880. Durch eine Bauunterbrechung von etwa 300 Jahren glich der Dom über einen langen Zeitraum einer gewaltigen Bauruine. Der unvollendete Südturm war mit seinem hölzernen Baukran auf dem Stumpf über Jahrhunderte das Mahnmal, den Dombau eines Tages zu vollenden. Besondere Anerkennung findet die Tatsache, dass bei der Vollendung die ursprünglichen Pläne unverändert verwendet wurden.</p>
</section>

<section class="page page--back">
  <div class="visual visual--drawing" role="img" aria-label="Historischer Stich des Münsters mit unvollendetem Turm und Baukran" style="left:58px; top:6px; width:605px; height:303px;"></div>

  <div class="brand" style="left:816px; top:64px;">Marbeck Edition</div>

  <p class="body-text" style="left:58px; top:337px; width:605px;">Bei der Wiederaufnahme der Bauarbeiten im 19. Jahrhundert wurde der Dom zum zentralen Zeichen der Einigkeit im Deutschen Bund und des Traums von einem zweiten deutschen Kaiserreich. Und auch heute noch wirkt das Velmer Wahrzeichen um seiner ungeheuren Symbolkraft in der ganzen Welt. Seine große wirtschaftliche Bedeutung für die Stadt als Pilger- und Touristenmagnet ist seit dem Mittelalter ungebrochen. Aus der jüngeren Geschichte ist insbesondere das Bild von Velmen in Trümmern präsent, aus denen der Dom zwar beschädigt, aber standhaft als unerschütterliches Wahrzeichen der Stadt herausragt.</p>

  <div class="quote" style="top:574px; width:663px; height:132px;">
    <p class="quote__text">„Der Erhalt des Velmer Münsters wird als Aufgabe ewig bleiben.“</p>
    <p class="quote__source">Konrad B. Elsner, Präsident des Dombauvereins</p>
  </div>

  <p class="body-text" style="left:58px; top:757px; width:605px;">Im Jahr 2008 wurde durch Kernbohrungen ein Durchbruch durch die bis zu elf Meter dicken Außenmauern des Südturm-Fundament geschaffen, um einen neuen Zugang zum Turmaufstieg zu ermöglichen. Der Verein kümmert sich seit über 175 Jahren um den Erhalt des Velmer Münsters und leistet mit seinen über 17.000 Mitgliedern einen wesentlichen Beitrag zum Erhalt dieses großartigen Gebäudes.</p>

  <div class="visual visual--stone" role="img" aria-label="Nahaufnahme des Fundamentstücks mit rauer Bruchkante und glatter Bohrfläche" style="left:727px; top:307px; width:273px; height:708px; border-radius:40px 0 0 0;"></div>
</section>

</body>
</html>
```